Automotive parts Package (box) design

We are developing a new packaging concept for our automotive service and suspension parts line. I will share 2–3 sample designs—some from other brands and some AI‑generated—and we need a designer to create a unified, original design direction based on these references.

We already have an established brand name, KEM, along with a logo. The logo may be updated or redesigned, but the brand name KEM must remain.

- The project includes creating the full packaging design for our product boxes, developing or refining the logo if needed.

-Then, after choosing the design, we will apply the same design to 8 boxes with small customisation for each box to match the product.

- The box die-lines will be provided by us.

Attached are a few sample designs. We need you to develop three or more new designs in a similar style. If you have additional creative concepts beyond these references, you are welcome to include them. The only fixed requirement is that the brand name KEM must remain unchanged in all proposed designs.

Box files such as PNG, PDF (ready-to-print file) and Ai (Editable/ Source file) and fonts with 3D mockup images at the end of the project must be given to us.

Target Market(s)

Car spare parts shops

Industry/Entity Type

Auto Parts

Requirements
Must have
• Our brand name KEM
Nice to have
• Package similar to big auto parts suppliers such as PLW, VARNE

```html
<!DOCTYPE html>
<html lang="en">
<head>
<meta charset="utf-8">
<title>KEM Service Parts – Box Panel</title>
<link rel="stylesheet" href="https://fonts.googleapis.com/css2?family=Montserrat:wght@600;700;800&family=Archivo+Black&family=Michroma&display=swap">
<style>
  :root{
    --page:#ffffff;
    --red:#d10a0f;
    --red-dark:#8e0508;
    --red-bright:#ff1a1a;
    --black:#0b0b0b;
    --grey-light:#f2f2f4;
    --grey-mid:#d5d6d9;
    --silver-1:#f4f4f4;
    --silver-2:#9a9ca0;
    --gold-1:#f6d25a;
    --gold-2:#c8901d;
    --white:#ffffff;
  }
  html,body{margin:0;padding:0;overflow:hidden;}
  body{width:694px;height:1200px;background:var(--page);position:relative;font-family:"Montserrat",sans-serif;}
  .panel{position:absolute;left:27px;top:421px;width:640px;height:357px;overflow:hidden;
    box-shadow:0 18px 40px rgba(0,0,0,.28);}
  .panel-shapes{position:absolute;inset:0;}
  .product-photo{position:absolute;left:396px;top:28px;width:214px;height:262px;border-radius:40px;
    background:radial-gradient(ellipse at 50% 48%,#b9bbbf 0%,#8d9095 45%,rgba(210,211,214,0) 75%);}
  .brand{position:absolute;left:40px;top:22px;color:var(--white);}
  .brand-name{font-family:"Montserrat",sans-serif;font-weight:800;font-size:58px;line-height:1;letter-spacing:1px;}
  .brand-sub{font-family:"Montserrat",sans-serif;font-weight:700;font-size:9.6px;margin-top:5px;letter-spacing:.2px;}
  .headline{position:absolute;left:26px;top:108px;margin:0;font-family:"Archivo Black",sans-serif;font-weight:400;
    font-size:55px;line-height:.93;letter-spacing:.5px;
    background:linear-gradient(100deg,var(--silver-2) 0%,var(--silver-1) 30%,#b7b9bd 55%,var(--silver-1) 80%,#a4a6aa 100%);
    -webkit-background-clip:text;background-clip:text;color:transparent;}
  .warranty-number{position:absolute;left:24px;top:246px;font-family:"Archivo Black",sans-serif;font-size:84px;line-height:1;
    color:var(--red);-webkit-text-stroke:1.5px #e6e6e6;}
  .warranty-month,.warranty-word{position:absolute;font-family:"Montserrat",sans-serif;font-weight:700;color:var(--black);}
  .warranty-month{left:100px;top:288px;font-size:12.5px;letter-spacing:.3px;}
  .warranty-word{left:98px;top:308px;font-size:10px;letter-spacing:.4px;}
  .tagline{position:absolute;left:250px;top:304px;font-family:"Michroma",sans-serif;font-size:11.6px;letter-spacing:2.4px;
    color:var(--red-bright);white-space:nowrap;}
</style>
</head>
<body>
  <section class="panel" aria-label="KEM Service Parts box front panel">
    <svg class="panel-shapes" width="640" height="357" viewBox="0 0 640 357" aria-hidden="true">
      <defs>
        <linearGradient id="redField" x1="0" y1="0" x2="1" y2="1">
          <stop offset="0" stop-color="#c9070c"/>
          <stop offset=".45" stop-color="#e0080d"/>
          <stop offset="1" stop-color="#9c0508"/>
        </linearGradient>
        <linearGradient id="greyField" x1="0" y1="0" x2="1" y2="1">
          <stop offset="0" stop-color="#ececef"/>
          <stop offset="1" stop-color="#f6f6f8"/>
        </linearGradient>
        <linearGradient id="bottomStrip" x1="0" y1="0" x2="1" y2="0">
          <stop offset="0" stop-color="#8e0508"/>
          <stop offset=".5" stop-color="#c0070b"/>
          <stop offset="1" stop-color="#ff1010"/>
        </linearGradient>
        <linearGradient id="goldBar" x1="0" y1="0" x2="1" y2="0">
          <stop offset="0" stop-color="#c8901d"/>
          <stop offset=".5" stop-color="#f6d25a"/>
          <stop offset="1" stop-color="#e0ae2f"/>
        </linearGradient>
        <linearGradient id="silverBar" x1="0" y1="0" x2="1" y2="0">
          <stop offset="0" stop-color="#a7a9ad"/>
          <stop offset=".5" stop-color="#f3f3f3"/>
          <stop offset="1" stop-color="#b5b7ba"/>
        </linearGradient>
      </defs>
      <rect class="grey-field" x="0" y="0" width="640" height="290" fill="url(#greyField)"/>
      <polygon class="red-field" points="0,0 326,0 380,283 0,283" fill="url(#redField)"/>
      <polygon class="red-field-shade" points="170,0 326,0 380,283 300,283" fill="#000" opacity=".08"/>
      <polygon class="silver-edge" points="326,0 334,0 388,283 380,283" fill="#c4c6c9"/>
      <polygon class="black-band" points="0,238 192,238 225,282 640,282 640,333 0,333" fill="var(--black)"/>
      <polyline class="band-edge" points="0,237 192,237 225,281 640,281" fill="none" stroke="#bfc1c4" stroke-width="1.2"/>
      <rect class="band-line" x="0" y="333" width="640" height="2" fill="#c9cacd"/>
      <rect class="bottom-strip" x="0" y="335" width="640" height="22" fill="url(#bottomStrip)"/>
      <polygon class="warranty-gold" points="96,285 196,285 208,304 96,304" fill="url(#goldBar)"/>
      <polygon class="warranty-silver" points="94,305 210,305 222,324 94,324" fill="url(#silverBar)"/>
      <g class="warranty-stars" fill="#f2b52b">
        <polygon points="101,272 102.6,276 107,276 103.5,278.6 104.8,283 101,280.4 97.2,283 98.5,278.6 95,276 99.4,276"/>
        <polygon points="113,272 114.6,276 119,276 115.5,278.6 116.8,283 113,280.4 109.2,283 110.5,278.6 107,276 111.4,276"/>
        <polygon points="125,272 126.6,276 131,276 127.5,278.6 128.8,283 125,280.4 121.2,283 122.5,278.6 119,276 123.4,276"/>
        <polygon points="137,272 138.6,276 143,276 139.5,278.6 140.8,283 137,280.4 133.2,283 134.5,278.6 131,276 135.4,276"/>
        <polygon points="149,272 150.6,276 155,276 151.5,278.6 152.8,283 149,280.4 145.2,283 146.5,278.6 143,276 147.4,276"/>
        <polygon points="161,272 162.6,276 167,276 163.5,278.6 164.8,283 161,280.4 157.2,283 158.5,278.6 155,276 159.4,276"/>
      </g>
    </svg>

    <div class="product-photo" role="img" aria-label="Product photo of a chrome V-twin engine on a light grey backdrop"></div>

    <div class="brand">
      <div class="brand-name">KEM</div>
      <div class="brand-sub">AUTOMOTIVE COMPONENTS</div>
    </div>

    <h1 class="headline">SERVICE<br>PARTS</h1>

    <div class="warranty-number">6</div>
    <div class="warranty-month">MONTH</div>
    <div class="warranty-word">WARRANTY</div>

    <div class="tagline">KEM AUTOMOTIVE COMPONENTS</div>
  </section>
</body>
</html>
```